Women's Online Clothing Boutique Needs Business Cards

I already have a logo that I would like to use. Some of the things that interest me is black business cards, foil embossed logo, glossy embossed logo, leopard print, no yellow font, rounded edges. I even like just a large logo on the front side with all of my information on the back side.

Contact Information for Business Card

https://silverheron.shopvenlo.com/
https://www.pagelink.net/thesilverheronboutique/
https://www.picfeed.net/thesilverheronboutique/
silverheronboutique@mailora.net

Requirements
Must have
• My Logo
Nice to have
• Leopard Print
Should not have
• No Yellow Font

```html
<!DOCTYPE html>
<html lang="en">
<head>
<meta charset="utf-8">
<title>The Silver Heron Boutique – Business Card</title>
<link rel="stylesheet" href="https://fonts.googleapis.com/css2?family=Jost:wght@400&display=swap">
<style>
  :root {
    --page: #eeeeee;
    --card: #262626;
    --gold: #c9962e;
    --gold-deep: #8a6a1f;
    --gold-bright: #e0aa35;
    --ink-light: #f2f2f2;
  }
  html, body {
    margin: 0;
    width: 1200px;
    height: 923px;
    overflow: hidden;
    background: var(--page);
    font-family: "Jost", sans-serif;
  }
  .canvas {
    position: relative;
    width: 1200px;
    height: 923px;
  }
  .card {
    position: absolute;
    left: 291px;
    width: 620px;
    height: 355px;
    border-radius: 18px;
    background: var(--card);
    overflow: hidden;
    box-shadow: 0 6px 14px rgba(0,0,0,0.25);
  }
  .card--front { top: 83px; }
  .card--back { top: 485px; }

  .print-area {
    position: absolute;
    inset: 0;
    background:
      radial-gradient(ellipse at 85% 50%, rgba(224,170,53,0.75), transparent 65%),
      linear-gradient(90deg, #4a3d1e 0%, #6b5424 45%, #a37c2a 100%);
  }
  .logo-panel {
    position: absolute;
    left: 129px;
    top: 76px;
    width: 363px;
    height: 204px;
    box-sizing: border-box;
    border: 2px solid var(--gold-deep);
    border-radius: 12px;
    background: var(--card);
    display: flex;
    flex-direction: column;
    align-items: center;
    justify-content: center;
  }
  .brand-name {
    margin: 0;
    color: var(--gold);
    font-weight: 400;
    text-align: center;
    line-height: 1.05;
  }
  .logo-panel .brand-name { font-size: 40px; }
  .brand-name .brand-sub { display: block; font-size: 0.75em; letter-spacing: 0.04em; }

  .back-brand {
    position: absolute;
    top: 48px;
    left: 0;
    right: 0;
  }
  .back-brand .brand-name { font-size: 40px; }

  .contact {
    position: absolute;
    left: 0;
    right: 0;
    top: 172px;
    display: flex;
    flex-direction: column;
    align-items: center;
    color: var(--ink-light);
    font-size: 18px;
    letter-spacing: 0.02em;
  }
  .contact-item {
    display: flex;
    flex-direction: column;
    align-items: center;
    margin-bottom: 6px;
  }
  .contact-icon {
    width: 20px;
    height: 20px;
    margin-bottom: 2px;
  }
  .contact-text { line-height: 22px; }
</style>
</head>
<body>
<main class="canvas">
  <section class="card card--front" aria-label="Card front">
    <div class="print-area" role="img" aria-label="Gold foil leopard print pattern on black"></div>
    <div class="logo-panel">
      <p class="brand-name">The Silver Heron<span class="brand-sub">Boutique</span></p>
    </div>
  </section>

  <section class="card card--back" aria-label="Card back">
    <div class="back-brand">
      <p class="brand-name">The Silver Heron<span class="brand-sub">Boutique</span></p>
    </div>
    <div class="contact">
      <div class="contact-item">
        <svg class="contact-icon" viewBox="0 0 20 20" aria-hidden="true">
          <circle cx="10" cy="10" r="8.5" fill="none" stroke="var(--gold)" stroke-width="1.6"/>
          <ellipse cx="10" cy="10" rx="3.5" ry="8.5" fill="none" stroke="var(--gold)" stroke-width="1.4"/>
          <line x1="1.5" y1="10" x2="18.5" y2="10" stroke="var(--gold)" stroke-width="1.4"/>
        </svg>
        <span class="contact-text">www.silverheron.shopvenlo.com</span>
      </div>
      <div class="contact-item">
        <svg class="contact-icon" viewBox="0 0 20 20" aria-hidden="true">
          <rect x="1" y="4" width="18" height="12" rx="1.5" fill="var(--gold)"/>
          <polyline points="1.5,5 10,11 18.5,5" fill="none" stroke="var(--card)" stroke-width="1.5"/>
        </svg>
        <span class="contact-text">silverheronboutique@mailora.net</span>
      </div>
      <div class="contact-item">
        <svg class="contact-icon" viewBox="0 0 20 20" aria-hidden="true">
          <rect x="2" y="2" width="16" height="16" rx="3" fill="var(--gold)"/>
        </svg>
        <span class="contact-text">thesilverheronboutique</span>
      </div>
    </div>
  </section>
</main>
</body>
</html>
```